Velmora Template Design for Wordpress Brightpath Site

We need graphic design and theme design work for our new site that will be running Brightpath with Velmora as the theme.

We have a draft logo that needs a graphic designer to improve it.

We are looking for sleek, modern, design that while minimal is distinct. ie page elements, content enhancement, block design that can be used, reused by in-house team.
This means there will also need to be a guide created on how to create, insert, edit each of those elements so that they can be used on new pages over time.

We have several businesses for which this is the "umbrella company" and so we will want to unify the colours and have identified a palette from which to start.

Some examples of site design we would like to stand up like:
https://www.tovrix.example/
https://pallorbranding.example/
https://business.skolvane.example/
https://www.fenwarrow.example/learning/home.aspx

When I say "coded" below, this really just means the CSS needed for page elements.

Target Market(s)

Small firms in professional services - engineers, land surveyors, consultants

Number of Pages Required

3 page

Font styles to use
Sans Serif

Requirements
Must have
• Wordpress/Velmora as base template, full home page layout with lorem ipsum placeholder
Nice to have
• custom blocks for pull quotes, call to action, a better design on the logo so it doesn't look like a rainbow.
Should not have
• Need for Structivo

```html
<!DOCTYPE html>
<html lang="en">
<head>
<meta charset="utf-8">
<title>Corvanta — Learning That Moves Organizations Forward</title>
<link rel="stylesheet" href="https://fonts.googleapis.com/css2?family=Figtree:wght@400;500;600&display=swap">
<style>
:root{
  --teal:#1a9bb0;
  --yellow:#fbb614;
  --ink:#1f1f1f;
  --body:#3a3a3a;
  --mist:#e4fbfd;
  --line:#d6d6d6;
  --white:#ffffff;
}
*{box-sizing:border-box;margin:0;padding:0}
html,body{width:1200px;height:4342px;overflow:hidden}
body{font-family:"Figtree",Arial,sans-serif;color:var(--ink);background:var(--white);position:relative}
.abs{position:absolute}
.accent{color:var(--teal)}
.btn{position:absolute;display:flex;align-items:center;justify-content:center;border-radius:30px;font-size:15px;font-weight:500;text-decoration:none;color:var(--ink)}
.btn-yellow{background:var(--yellow)}
.btn-teal{background:var(--teal);color:var(--white)}
.btn-outline{border:1.5px solid #444;background:var(--white)}
.photo{position:absolute;border-radius:22px}

/* header */
.brand{font-size:38px;font-weight:500;color:var(--ink);letter-spacing:-.5px}
.nav{position:absolute;top:36px;left:300px;display:flex;font-size:15px;color:#444}
.nav span{padding:0 18px;border-right:1px solid #e2e2e2;line-height:24px}
.nav span:last-child{border-right:none}
.nav .current{color:var(--teal)}

/* hero */
.hero-title{top:156px;left:0;width:1200px;text-align:center;font-size:49px;font-weight:500;line-height:56px}
.hero-text{top:292px;left:190px;width:820px;text-align:center;font-size:18px;line-height:28px;color:var(--body)}

h2.sec{position:absolute;font-size:38px;font-weight:500;line-height:46px}
.copy{font-size:14.5px;line-height:27px;color:var(--body)}

/* ecosystem list */
.points{top:1104px;left:152px;width:940px;list-style:none}
.points li{position:relative;padding-left:40px;margin-bottom:16px}
.points svg{position:absolute;left:0;top:6px}

/* impact band */
.impact{top:1867px;left:0;width:1200px;height:659px;background:var(--mist)}
.pillar{position:absolute;top:2187px;width:300px;text-align:center}
.pillar .icon{width:64px;height:64px;margin:0 auto;border-radius:8px;background:#a8eef6;display:flex;align-items:center;justify-content:center}
.pillar h3{font-size:18px;font-weight:600;margin-top:30px}
.pillar p{font-size:14.5px;line-height:27px;color:var(--body);margin-top:16px}
.divider{position:absolute;top:2165px;height:250px;border-left:1.5px dashed #9aa}

/* insight cards */
.card{position:absolute;top:2846px;width:300px;height:411px;background:var(--white);border-radius:20px;box-shadow:0 4px 18px rgba(0,0,0,.12)}
.card .thumb{position:absolute;top:24px;left:20px;width:260px;height:185px;border-radius:20px}
.card h3{position:absolute;top:236px;left:26px;width:200px;font-size:16px;font-weight:600;line-height:23px}
.card .go{position:absolute;top:240px;left:226px}
.card p{position:absolute;top:296px;left:26px;width:250px;font-size:14.5px;line-height:23px;color:var(--body)}

/* cta */
.cta-photo{top:3459px;left:0;width:1200px;height:543px;background:linear-gradient(100deg,#3a3e3c 0%,#b59a5f 40%,#5b6c55 65%,#3a3b3e 100%)}
.cta-card{top:3559px;left:66px;width:490px;height:355px;background:var(--white);border-radius:24px}

/* footer */
.foot-nav{position:absolute;top:4090px;left:520px;width:570px;display:flex;justify-content:space-between;font-size:15px;color:#333}
.social{position:absolute;top:4168px;width:36px;height:36px;border-radius:50%;background:var(--teal)}
.legal{top:4302px;left:0;width:1200px;height:40px;background:var(--teal);color:var(--white);font-size:14px;display:flex;align-items:center;justify-content:center}
</style>
</head>
<body>

<!-- Header -->
<div class="abs brand" style="top:24px;left:96px">Corvanta</div>
<nav class="nav">
  <span class="current">Home</span><span>Our Approach</span><span>Our Brands</span><span>Insights</span><span>About</span><span>Contact</span>
</nav>
<a class="btn btn-yellow" style="top:24px;left:910px;width:193px;height:50px">Explore Solutions</a>

<!-- Hero -->
<h1 class="abs hero-title" style="font-weight:500">Learning That Moves <span class="accent">Organizations</span><br>Forward</h1>
<p class="abs hero-text">Corvanta is the umbrella platform uniting specialized learning brands to help organizations build capability, develop leaders, and drive measurable performance.</p>
<a class="btn btn-teal" style="top:382px;left:367px;width:245px;height:50px">Explore Our Solutions</a>
<a class="btn btn-outline" style="top:382px;left:635px;width:196px;height:50px">Partner With Us</a>

<div class="photo" role="img" aria-label="Hands reviewing a printed business report with charts beside a coffee cup" style="top:516px;left:113px;width:300px;height:389px;background:linear-gradient(160deg,#cfd7dc,#8fa3b3 55%,#6b7a86)"></div>
<div class="photo" role="img" aria-label="Team of colleagues smiling around a meeting table with a laptop" style="top:516px;left:445px;width:645px;height:389px;background:linear-gradient(120deg,#6d7a6a,#9a8e7a 45%,#4f5652)"></div>

<!-- Ecosystem -->
<h2 class="sec" style="top:1030px;left:152px">An Ecosystem of <span class="accent">Strategic</span> Learning</h2>
<ul class="abs points copy">
  <li><svg width="24" height="14" viewBox="0 0 24 14"><path d="M1 7h20M15 1l6 6-6 6" stroke="#fbb614" stroke-width="2" fill="none"/></svg>Corvanta brings together a portfolio of focused learning and development businesses under one unified vision: creating learning systems that support long-term organizational growth.</li>
  <li><svg width="24" height="14" viewBox="0 0 24 14"><path d="M1 7h20M15 1l6 6-6 6" stroke="#fbb614" stroke-width="2" fill="none"/></svg>Each brand within the Corvanta ecosystem addresses a specific challenge — from leadership development to professional capability building — while remaining connected through a shared approach, design philosophy, and commitment to outcomes.</li>
</ul>

<!-- Specialized -->
<div class="photo" role="img" aria-label="Engineer working at dual monitors showing a technical model" style="top:1331px;left:111px;width:435px;height:415px;background:linear-gradient(135deg,#8fb0c8,#3d5a74 55%,#1f2a38);border-bottom:3px solid var(--yellow)"></div>
<h2 class="sec" style="top:1338px;left:597px">Specialized <span class="accent">Expertise.</span><br>Unified Vision.</h2>
<div class="abs copy" style="top:1454px;left:597px;width:490px">
  <p>Each Corvanta brand operates with depth and focus, while contributing to a broader learning ecosystem designed to support organizations at every stage of growth.</p>
  <p style="margin-top:19px">Each brand within the Corvanta ecosystem addresses a specific challenge — from leadership development to professional capability building — while remaining connected through a shared approach, design philosophy, and commitment to outcomes.</p>
</div>
<a class="btn btn-yellow" style="top:1693px;left:597px;width:219px;height:48px">Explore Our Brands →</a>

<!-- Impact -->
<section class="abs impact"></section>
<h2 class="sec" style="top:1954px;left:0;width:1200px;text-align:center">Designed for Impact. <span class="accent">Built</span> for Scale.</h2>
<p class="abs copy" style="top:2034px;left:185px;width:830px;text-align:center">Each brand within the Corvanta ecosystem addresses a specific challenge — from leadership development to professional capability building — while remaining connected through a shared approach, design philosophy, and commitment to outcomes.</p>

<div class="pillar" style="left:113px">
  <div class="icon"><svg width="40" height="40" viewBox="0 0 40 40" fill="none" stroke="#1f5d6a" stroke-width="2"><path d="M4 20l8-8 8 4 8-4 8 8-10 10-6-4-6 4z"/><path d="M14 24l4 4M18 22l4 4"/></svg></div>
  <h3>Strategic Alignment</h3>
  <p>Learning starts with business goals. Every program is intentionally designed to support real organizational priorities.</p>
</div>
<div class="divider" style="left:436px"></div>
<div class="pillar" style="left:456px">
  <div class="icon"><svg width="40" height="40" viewBox="0 0 40 40" fill="none" stroke="#1f5d6a" stroke-width="2"><path d="M6 12h12a2 2 0 012 2v20a2 2 0 00-2-2H6zM34 12H22a2 2 0 00-2 2v20a2 2 0 012-2h12z"/><circle cx="20" cy="6" r="3"/></svg></div>
  <h3>Applied Learning</h3>
  <p>We focus on practical, experience-based learning that translates into action — not theory</p>
</div>
<div class="divider" style="left:775px"></div>
<div class="pillar" style="left:801px">
  <div class="icon"><svg width="40" height="40" viewBox="0 0 40 40" fill="none" stroke="#1f5d6a" stroke-width="2"><rect x="4" y="6" width="28" height="22" rx="2"/><path d="M10 22v-4M16 22v-8M22 22v-6"/><circle cx="28" cy="28" r="5"/><path d="M32 32l4 4"/></svg></div>
  <h3>Sustainable Growth</h3>
  <p>Our learning systems are designed to evolve alongside your organization, supporting long-term capability</p>
</div>

<!-- Insights -->
<h2 class="sec" style="top:2643px;left:0;width:1200px;text-align:center">Our Featured <span class="accent">Insights</span></h2>
<p class="abs copy" style="top:2712px;left:130px;width:940px;text-align:center">Learning is evolving — and organizations that treat it as a strategic system, not a series of events, are the ones that move forward with confidence. The Corvanta Insights hub explores how learning, leadership, and organizational capability intersect. We share perspectives, research, and practical thinking to help leaders design learning systems that deliver real-world impact.</p>

<article class="card" style="left:113px">
  <div class="thumb" role="img" aria-label="Hand arranging wooden blocks with business icons and a rising chart" style="background:linear-gradient(135deg,#6f8ea8,#a88a68 60%,#5b4a3a)"></div>
  <h3>Learning as a Strategic Advantage</h3>
  <svg class="go" width="22" height="14" viewBox="0 0 22 14"><path d="M1 7h18M13 1l6 6-6 6" stroke="#fbb614" stroke-width="2" fill="none"/></svg>
  <p>When learning is aligned with business priorities, it becomes a competitive advantage rather than a cost center.</p>
</article>
<article class="card" style="left:452px">
  <div class="thumb" role="img" aria-label="Professionals focused on work in an open office" style="background:linear-gradient(135deg,#5e7688,#9aa6ae 50%,#3c4650)"></div>
  <h3>Building Capability in a Changing Workplace</h3>
  <svg class="go" width="22" height="14" viewBox="0 0 22 14"><path d="M1 7h18M13 1l6 6-6 6" stroke="#fbb614" stroke-width="2" fill="none"/></svg>
  <p>When learning is aligned with business priorities, it becomes a competitive advantage rather than a cost center.</p>
</article>
<article class="card" style="left:790px">
  <div class="thumb" role="img" aria-label="Hand holding a tablet showing performance charts" style="background:linear-gradient(135deg,#b54a3a,#e2e6ec 55%,#4c6a90)"></div>
  <h3>Measuring What Matters in Learning</h3>
  <svg class="go" width="22" height="14" viewBox="0 0 22 14"><path d="M1 7h18M13 1l6 6-6 6" stroke="#fbb614" stroke-width="2" fill="none"/></svg>
  <p>When learning is aligned with business priorities, it becomes a competitive advantage rather than a cost center.</p>
</article>
<a class="btn btn-yellow" style="top:3309px;left:489px;width:217px;height:49px">Read More Insights</a>

<!-- CTA -->
<div class="abs cta-photo" role="img" aria-label="Group of colleagues in a relaxed circle discussion in a bright workspace"></div>
<div class="abs cta-card">
  <h2 class="sec" style="top:44px;left:47px;line-height:50px">Ready to Build What’s<br><span class="accent">Next?</span></h2>
  <p class="abs copy" style="top:168px;left:47px;width:405px">Whether you’re exploring one of our specialized brands or looking for a strategic partner to unify your learning approach, Corvanta is designed to help organizations move</p>
  <a class="btn btn-yellow" style="top:268px;left:47px;width:219px;height:48px">Start a Conversation</a>
</div>

<!-- Footer -->
<div class="abs brand" style="top:4085px;left:113px">Corvanta</div>
<div class="social" style="left:113px" aria-label="Social link one"></div>
<div class="social" style="left:157px" aria-label="Social link two"></div>
<div class="social" style="left:201px" aria-label="Social link three"></div>
<nav class="foot-nav"><span>Home</span><span>Our Approach</span><span>Our Brands</span><span>Insights</span><span>About</span><span>Contact</span></nav>
<div class="abs" style="top:4132px;left:586px;width:501px;border-top:2px solid var(--teal)"></div>
<p class="abs copy" style="top:4150px;left:490px;width:600px;text-align:right">A unified learning ecosystem designed to help organizations build capability, develop leaders, and drive meaningful performance through intentional learning systems.</p>
<div class="abs legal">Corvanta © All rights reserved. | Privacy | Terms</div>

</body>
</html>
```